Webdesign für Arztpraxis
Zielgruppe
Arztpraxis für Dermatologie am Solvana.
Solvana ist ein Spital/Krankenhaus hier in Basel, Schweiz.
Kunden sind in jeder Altersstufe für Hauterkrankungen.
Behandlung Chirugisch, konservativ und mit Laser.
Aufgabenstellung
Brandguide und Logo anbei
Farben: #395722 und #ABCF8A
Beispielseite, die gefällt: https://hautpraxis-morvan-tigges.de

```html
<!DOCTYPE html>
<html lang="de">
<head>
<meta charset="utf-8">
<title>Hautarztpraxis – Öffnungszeiten und Blog</title>
<link rel="stylesheet" href="https://fonts.googleapis.com/css2?family=Poppins:wght@300;400;500;600&display=swap">
<style>
  :root {
    --brand-dark: #395722;
    --brand-light: #abcf8a;
    --brand-light-text: #8dbb66;
    --cv-bg: #e7f0dd;
    --page-white: #ffffff;
    --blog-bg: #f3f7f6;
    --card-grey: #efefef;
    --card-border: #e4e4e4;
    --muted-text: #a9a9a9;
    --nav-grey: #c7c7c7;
    --ink: #111111;
    --cv-ink: #333333;
  }
  * { margin: 0; padding: 0; box-sizing: border-box; }
  html, body {
    width: 1200px; height: 656px; overflow: hidden;
    font-family: "Poppins", sans-serif; background: var(--page-white); color: var(--ink);
  }
  .page { position: relative; width: 1200px; height: 656px; overflow: hidden; }

  /* CV section */
  .cv-section {
    position: absolute; left: 0; top: 0; width: 1200px; height: 200px;
    background: var(--cv-bg);
  }
  .cv-list { position: absolute; left: 180px; top: -8px; list-style: none; }
  .cv-entry { font-size: 10.5px; line-height: 16px; color: var(--cv-ink); margin-bottom: 15px; }

  /* Opening hours */
  .hours-section { position: absolute; left: 0; top: 200px; width: 1200px; height: 270px; }
  .section-label { text-align: center; font-size: 8px; color: var(--brand-light-text); }
  .hours-section .section-label { position: absolute; top: 56px; width: 100%; }
  .section-title { text-align: center; font-weight: 500; font-size: 15px; }
  .hours-section .section-title { position: absolute; top: 66px; width: 100%; }
  .hours-row {
    position: absolute; left: 166px; top: 92px; display: flex; gap: 12px;
  }
  .day-card {
    width: 163px; height: 64px; background: var(--card-grey);
    border: 1px solid var(--card-border); border-radius: 3px;
    display: flex; flex-direction: column; align-items: center; justify-content: center;
    color: var(--muted-text); font-weight: 300; font-size: 14px; line-height: 19px;
  }
  .slider-arrow {
    position: absolute; top: 114px; width: 21px; height: 21px; border-radius: 50%;
    background: var(--nav-grey); display: flex; align-items: center; justify-content: center;
  }
  .slider-arrow.prev { left: 155px; }
  .slider-arrow.next { left: 1022px; }
  .booking-button {
    position: absolute; left: 526px; top: 196px; width: 148px; height: 29px;
    border: 1px solid var(--brand-light); border-radius: 15px;
    display: flex; align-items: center; justify-content: center; gap: 14px;
    font-size: 10px; color: var(--brand-light-text);
  }

  /* Blog */
  .blog-section {
    position: absolute; left: 0; top: 470px; width: 1200px; height: 186px;
    background: var(--blog-bg);
  }
  .blog-section .section-label {
    position: absolute; top: 29px; width: 100%; color: var(--brand-dark); font-weight: 500; padding-left: 0;
    left: -11px;
  }
  .blog-section .section-title { position: absolute; top: 40px; width: 100%; font-weight: 600; }
  .post-row { position: absolute; left: 166px; top: 72px; display: flex; gap: 23px; }
  .post-card { position: relative; width: 274px; height: 130px; border-radius: 4px 4px 0 0; overflow: hidden; }
  .post-image { position: absolute; inset: 0; }
  .post-image.skin-check { background: linear-gradient(100deg, #d9dfe3 0%, #cfd5da 40%, #35476a 65%, #e9ecef 100%); }
  .post-image.nutrition { background: linear-gradient(120deg, #c7651f 0%, #e49a2c 30%, #7d8a2e 55%, #e9712b 80%, #9a3b2a 100%); }
  .post-image.mole-exam { background: linear-gradient(100deg, #6f7a5f 0%, #e8e4de 35%, #c9b49b 70%, #b9aa98 100%); }
  .post-date {
    position: absolute; left: 11px; top: 7px; width: 44px; height: 44px;
    background: var(--brand-dark); border-radius: 4px; color: #fff;
    display: flex; flex-direction: column; align-items: center; justify-content: center;
    font-size: 10px; line-height: 12px;
  }
  .post-date strong { font-weight: 600; }
</style>
</head>
<body>
<main class="page">
  <section class="cv-section">
    <ul class="cv-list">
      <li class="cv-entry">Promotion zum Dr. med. 11/2012<br>Nordhain-Universität Elbstadt/ Lindenklinik (D)</li>
      <li class="cv-entry">Weiterbildungsassistent Dermatologie 05/2005 - 05/2010<br>in der Hautklinik am Klinikum Ravensfeld (D)<br>und an der Universitätshautklinik Kesselberg (D)</li>
      <li class="cv-entry">Studium der Humanmedizin &nbsp; 10/1998 - 05/2005<br>an der Auental-Universität Kesselberg (D)<br>und im Kantonsspital Seewiler</li>
    </ul>
  </section>

  <section class="hours-section">
    <p class="section-label">Praxis</p>
    <h2 class="section-title">Öffnungszeiten</h2>
    <div class="hours-row">
      <div class="day-card"><span>Montag</span><span>8:30-17:00</span></div>
      <div class="day-card"><span>Dienstag</span><span>8:30-17:00</span></div>
      <div class="day-card"><span>Mittwoch</span><span>8:30-17:00</span></div>
      <div class="day-card"><span>Donnerstag</span><span>8:30-17:00</span></div>
      <div class="day-card"><span>Freitag</span><span>8:30-17:00</span></div>
    </div>
    <span class="slider-arrow prev"><svg width="8" height="10" viewBox="0 0 8 10"><path d="M5.5 1.5 2 5l3.5 3.5" fill="none" stroke="#fff" stroke-width="1.4"/></svg></span>
    <span class="slider-arrow next"><svg width="8" height="10" viewBox="0 0 8 10"><path d="M2.5 1.5 6 5 2.5 8.5" fill="none" stroke="#fff" stroke-width="1.4"/></svg></span>
    <a class="booking-button">Online Termine
      <svg width="10" height="8" viewBox="0 0 10 8"><path d="M0.5 4h8.5M6 1l3 3-3 3" fill="none" stroke="#8dbb66" stroke-width="1"/></svg>
    </a>
  </section>

  <section class="blog-section">
    <p class="section-label">Blog</p>
    <h2 class="section-title">Unsere neuesten und beliebtesten Tipps und Tricks für Sie</h2>
    <div class="post-row">
      <article class="post-card">
        <div class="post-image skin-check" role="img" aria-label="Foto: Hautuntersuchung eines Patienten mit Dermatoskop und Monitor in heller Praxis"></div>
        <div class="post-date"><strong>17</strong><span>Nav</span></div>
      </article>
      <article class="post-card">
        <div class="post-image nutrition" role="img" aria-label="Foto: gesunde Lebensmittel mit Obst, Gemüse und Beeren"></div>
        <div class="post-date"><strong>16</strong><span>Nav</span></div>
      </article>
      <article class="post-card">
        <div class="post-image mole-exam" role="img" aria-label="Foto: Ärztin untersucht Muttermale am Rücken einer Patientin mit Lupe"></div>
        <div class="post-date"><strong>15</strong><span>Nav</span></div>
      </article>
    </div>
  </section>
</main>
</body>
</html>
```